Fatigued and Overloaded by COVID Messages? We need original illustrations to show that.

Everywhere you look there are messages about COVID. That is leading many people to feel fatigued and overloaded by the messages.

We surveyed U.S. adults March 20th - 24th, 2020 and measured message fatigue, information overload, perceived repetition, and perceived exaggeration. Here is how participants responded:

When it comes to coronavirus . . .
55% feel exhausted by all the messages.
54% feel overloaded by the amount of information.
51% feel that the messages are repetitive.
47% feel like messages exaggerate how bad it is.

In other words, almost half of U.S. adults show signs of message fatigue, information overload, perceived message repetition, and perceived message exaggeration.

We will continue to survey 400 adults every week for the next 16 weeks. Each time we will measure message fatigue, information overload, perceived repetition, and perceived exaggeration. We expect that it will increase over time.

What are we looking for? We need innovative and original illustrations that attempt to communicate these findings. The illustrations would visualize message fatigue, information overload, perceived message repetition, and perceived message exaggeration.

What sort of visual are we looking for? Our preference is for an original illustration (or set of illustrations). Our preference is for creative and powerful illustrations, but we are also open to the creative and well-executed infographics.

We need these images fast . We will award monetary prizes to the 3 best designs. If we like more than that, then we might purchase more (e.g., in past contests, we have purchased as many as 30 designs).

What we will need:
(1) The illustrations must be original and we will need the photoshop and/or illustrator files for all artwork. (By original, we mean that the illustrations are 100% created by you. Our organization requires that we utilize only original illustrated work. We have had issues with free imagery being pirated and reposted as free. We sidestep that issue by just having everything created.)

(2) The illustration should say, somewhere: "Based on a survey of 400 U.S. adults conducted March 20 - 24th, 2020."

(3) We will have almost 4 months worth of data by the time this is done. In other words, the illustrations might be able to help us present that weekly data.

(4) We have conducted other Artvendo projects. It might be helpful to examine designs we liked in the past. For example, here is another COVID project we just finished:

https://jobs.artvendo-example.com/job/5162048

Target Market(s)

U.S. adults

Requirements
Must have
• Original illustrations. Mobile friendly design. People will view this on their smartphones.
Nice to have
• A design that we can use to communicate the data across time.

```html
<!DOCTYPE html>
<html lang="en">
<head>
<meta charset="utf-8">
<title>Fatigued and Overloaded by COVID Messages?</title>
<link rel="stylesheet" href="https://fonts.googleapis.com/css2?family=Montserrat:ital,wght@0,500;0,600;0,700;1,600&display=swap">
<style>
  :root {
    --brand-blue: #0367b0;
    --bar-red: #e44a3e;
    --bar-blue: #55a7cc;
    --panel-grey: #d1d2d4;
    --ink: #111111;
    --white: #ffffff;
    --art-tone: #ec8178;
  }
  * { box-sizing: border-box; margin: 0; padding: 0; }
  html, body { width: 848px; height: 1200px; overflow: hidden; background: var(--white); }
  body { font-family: "Montserrat", Arial, sans-serif; color: var(--ink); }
  .poster { position: relative; width: 848px; height: 1200px; }

  .masthead {
    position: absolute; left: 116px; top: 77px; width: 638px; height: 113px;
    background: var(--brand-blue); color: var(--white); text-align: center;
  }
  .masthead__title { font-size: 23.5px; font-weight: 700; margin-top: 24px; letter-spacing: 0.1px; line-height: 28px; }
  .masthead__lede {
    font-size: 10.8px; font-style: italic; font-weight: 600; line-height: 12.8px;
    margin-top: 12px;
  }

  .intro {
    position: absolute; left: 116px; width: 638px; top: 212px;
    text-align: center; font-size: 25px; font-weight: 600; line-height: 32px;
  }

  .stat {
    position: absolute; left: 158px; width: 555px; height: 119px;
    background: var(--bar-blue); display: flex;
  }
  .stat__red { position: relative; height: 100%; background: var(--bar-red); flex: none; }
  .stat__art { position: absolute; top: 10px; bottom: 10px; background: var(--art-tone); border-radius: 4px; }
  .stat__figure {
    position: absolute; top: 50%; transform: translateY(-50%);
    color: var(--white); font-size: 40px; font-weight: 700; letter-spacing: -0.5px; line-height: 1;
  }
  .stat__label {
    align-self: center; padding-left: 16px; font-size: 16.8px; font-weight: 500;
    line-height: 19px; letter-spacing: 0.3px;
  }
  .stat--exhausted { top: 303px; }
  .stat--exhausted .stat__red { width: 305px; }
  .stat--exhausted .stat__art { left: 30px; width: 130px; }
  .stat--exhausted .stat__figure { right: 19px; }
  .stat--overloaded { top: 465px; }
  .stat--overloaded .stat__red { width: 300px; }
  .stat--overloaded .stat__art { left: 26px; width: 145px; }
  .stat--overloaded .stat__figure { right: 11px; }
  .stat--repetitive { top: 628px; }
  .stat--repetitive .stat__red { width: 283px; }
  .stat--repetitive .stat__art { left: 24px; width: 150px; }
  .stat--repetitive .stat__figure { right: 11px; }
  .stat--exaggerated { top: 791px; }
  .stat--exaggerated .stat__red { width: 261px; }
  .stat--exaggerated .stat__art { left: 8px; width: 145px; }
  .stat--exaggerated .stat__figure { right: 5px; }
  .stat--repetitive .stat__label, .stat--exaggerated .stat__label { padding-left: 12px; }

  .summary {
    position: absolute; left: 116px; top: 945px; width: 638px; height: 125px;
    background: var(--panel-grey);
  }
  .summary__map {
    position: absolute; left: 37px; top: 39px; width: 112px; height: 63px; border-radius: 6px;
    background: linear-gradient(90deg, var(--bar-blue) 0%, var(--bar-blue) 48%, var(--bar-red) 52%, var(--bar-red) 100%);
  }
  .summary__heading { position: absolute; left: 166px; top: 15px; font-size: 19px; font-weight: 600; line-height: 24px; }
  .summary__text {
    position: absolute; left: 163px; top: 41px; width: 470px;
    font-size: 16.8px; font-weight: 500; line-height: 19px; letter-spacing: 0.2px;
  }

  .source {
    position: absolute; left: 116px; top: 1070px; width: 638px; height: 37px;
    background: var(--brand-blue); color: var(--white);
    font-size: 14.2px; font-weight: 500; text-align: center; line-height: 37px; letter-spacing: 0.2px;
  }
</style>
</head>
<body>
<main class="poster">
  <header class="masthead">
    <h1 class="masthead__title">Fatigued and Overloaded by COVID Messages?</h1>
    <p class="masthead__lede">We surveyed U.S. adults March 20th - 24th, 2020 a<br>nd measured message fatigue, information overload,<br>perceived repetition, and perceived exaggeration.</p>
  </header>

  <h2 class="intro">When it comes to coronavirus . . .</h2>

  <section class="stat stat--exhausted">
    <div class="stat__red">
      <div class="stat__art" role="img" aria-label="Illustration of a tired person looking at a phone"></div>
      <span class="stat__figure">55%</span>
    </div>
    <p class="stat__label">feel exhausted<br>by all the messages.</p>
  </section>

  <section class="stat stat--overloaded">
    <div class="stat__red">
      <div class="stat__art" role="img" aria-label="Illustration of a person at a laptop surrounded by notification icons"></div>
      <span class="stat__figure">54%</span>
    </div>
    <p class="stat__label">feel overloaded by<br>the amount<br>of information.</p>
  </section>

  <section class="stat stat--repetitive">
    <div class="stat__red">
      <div class="stat__art" role="img" aria-label="Illustration of a person with a phone and many forwarding arrows"></div>
      <span class="stat__figure">51%</span>
    </div>
    <p class="stat__label">feel that the messages<br>are repetitive</p>
  </section>

  <section class="stat stat--exaggerated">
    <div class="stat__red">
      <div class="stat__art" role="img" aria-label="Illustration of a sceptical person with a phone surrounded by alarming news icons"></div>
      <span class="stat__figure">47%</span>
    </div>
    <p class="stat__label">feel like messages<br>exaggerate how bad it is</p>
  </section>

  <section class="summary">
    <div class="summary__map" role="img" aria-label="Map of the United States split half blue and half red"></div>
    <h3 class="summary__heading">In other words</h3>
    <p class="summary__text">almost half of U.S. adults show signs of message fatigue, information overload, perceived message repetition, and perceived message exaggeration.</p>
  </section>

  <footer class="source">Based on a survey of 400 U.S. adults conducted March 20 - 24th, 2020</footer>
</main>
</body>
</html>
```